One of a kind, 100% Pure & Natural Skincare line needs stunning product label

We need product label design for new natural skincare company called Tobin & Lusa Skincare. We create luxurious, 100% pure & natural skincare that is free from ingredients that may be potentially irritating to the skin. No toxins, preservatives or additives. Our initial product is Meadowlight Face Balm, a nourishing face cream that suits discerning women with mature skin and those with dry/sensitive skin needing extra hydration. Also those that choose to minimize their exposure to environmental toxins. Our brand is simple yet elegant, supporting a holistic, authentic lifestyle and embracing natural skincare.

Target Market(s)

Discerning women with mature skin and those with dry/sensitive skin needing extra hydration. Also those that choose to minimize their exposure to environmental toxins.

Industry/Entity Type

Skin Care Product

Font styles to use
Sans Serif
Script

Colors
f9d9e8
fef1ee

Requirements
Must have
• The Logo.
MEADOWLIGHT FACE BALM
EMBRACING NATURAL SKINCARE
Labels must be feminine, simple/minimal yet stylish. Uncluttered yet elegant.
This is a very natural product with minimal ingredients.
Nice to have
• The logo can be incorporated in to the label, or It can be left separate as a sticker on top of the jar. The product is a firm balm consistency and is in frosted glass jars with matt silver lids.
Jar height is 45mm, width is 60mm.
Label height: 28mm and length 185mm
Should not have
• Natural or farmers market type theme. No Bold/loud lettering.

```html
<!DOCTYPE html>
<html lang="en">
<head>
<meta charset="utf-8">
<title>Tobin &amp; Lusa Skincare – Meadowlight Face Balm Label</title>
<link rel="stylesheet" href="https://fonts.googleapis.com/css2?family=Oswald:wght@300;400&family=Arimo:wght@400;700&display=swap">
<style>
  :root {
    --paper: #ffffff;
    --blush-light: #fbe3ee;
    --blush: #f4c3d8;
    --blush-deep: #efb1cb;
    --accent-pink: #f29bb6;
    --ink-grey: #6a6a6a;
    --ink-dark: #222222;
    --ink-navy: #1c1230;
    --lotus-a: #fbeaf1;
    --lotus-b: #f2c9da;
  }
  * { margin: 0; padding: 0; box-sizing: border-box; }
  html, body { width: 1200px; height: 1002px; overflow: hidden; }
  body { background: var(--paper); }
  .label {
    position: relative;
    width: 1200px;
    height: 1002px;
    overflow: hidden;
    background: linear-gradient(to bottom,
      var(--paper) 0%,
      var(--paper) 22%,
      var(--blush-light) 55%,
      var(--blush) 85%,
      var(--blush-deep) 100%);
  }
  .brand-name {
    position: absolute;
    left: 0;
    width: 1200px;
    top: 262px;
    text-align: center;
    font-family: "Oswald", sans-serif;
    font-weight: 300;
    font-size: 64px;
    letter-spacing: 4px;
    color: var(--ink-dark);
  }
  .product-title {
    position: absolute;
    left: 0;
    width: 1200px;
    top: 488px;
    text-align: center;
    font-family: "Oswald", sans-serif;
    font-weight: 400;
    font-size: 52px;
    line-height: 78px;
    color: var(--ink-grey);
    text-transform: uppercase;
  }
  .product-title .accent { color: var(--accent-pink); }
  .lotus-art {
    position: absolute;
    left: 378px;
    top: 640px;
    width: 444px;
    height: 250px;
  }
  .volume {
    position: absolute;
    left: 900px;
    top: 840px;
    font-family: "Arimo", sans-serif;
    font-weight: 700;
    font-size: 31px;
    color: var(--ink-navy);
  }
  .claim {
    position: absolute;
    left: 0;
    width: 1200px;
    top: 904px;
    text-align: center;
    font-family: "Arimo", sans-serif;
    font-weight: 400;
    font-size: 37px;
    color: var(--ink-dark);
  }
</style>
</head>
<body>
  <main class="label">
    <div class="brand-name">Tobin &amp; Lusa Skincare</div>

    <h1 class="product-title">
      <span>Meadowlight Face Balm</span><br>
      <span>Embracing Natural <span class="accent">Skincare</span></span>
    </h1>

    <svg class="lotus-art" role="img" aria-label="Faint pale pink lotus flower illustration" viewBox="0 0 444 250">
      <defs>
        <radialGradient id="lotusGlow" cx="50%" cy="55%" r="55%">
          <stop offset="0%" stop-color="var(--lotus-b)" stop-opacity="0.85"/>
          <stop offset="100%" stop-color="var(--lotus-a)" stop-opacity="0"/>
        </radialGradient>
      </defs>
      <ellipse cx="222" cy="130" rx="222" ry="120" fill="url(#lotusGlow)"/>
    </svg>

    <div class="volume">50ML</div>
    <p class="claim">100% pure &amp; natural</p>
  </main>
</body>
</html>
```